Zestro Design Award - $10,000 tablet app design contest, Retail Catalogue Category

Zestro is a marketplace for Slatebook App Templates (similar to PageForge templates). We want you to design an app template for sale in our marketplace which targets Retail Catalogue Apps (Slatebook Apps that are created for Product Catalogues. For example: paint, clothing… etc).

It’s up to you to create pages or features for the App Template that you think are appropriate. Creativity will be rewarded! Here are some example pages or features that you could create:

• Welcome page
• Features
• Product pages
• Product details
• Share products on Friendlane
• Maps – store locations or events
• Social media integration
• Animations and video

Your design should be Vibrant, Engaging and Contemporary. If you have an Slatebook, download Zestro Lens and download template examples in the download tab.

Your entry must include:
• A brief description of your template
• Preview images of all pages of your template

Attached to this project are free templates to help you get started with your design. We have included:
1. A free portfolio template for designers/photographers
2. Icons and artwork to use in your template
3. Blank pages template
4. Form template
5. Video ad template

If you are selected as a finalist you will be required to submit an .zproject file containing:
• Your LayoutPro source files
• Preview images of your template
• All creative / stock assets used in the template (animations, video etc.)
• A text file with instructions on how to update the template
• A metadata .txt file containing template details and your information

How to enter:
1. Register at Marketplace and view the instructions under the welcome message https://market.zestrobase.example/welcome
2. Download Zestro Builder: https://help.zestrobase.example/entries/48175209-zestro-builder
3. Use the free templates provided in this brief to create your designs and submit to ArtPluvia
Updates

Project Deadline Extended
Reason: Due to the Christmas break we are extending the deadline of our competition. Thank you for time and effort - I will be providing feedback over the next couple of days! Best wishes, Melody

Hi All,

I have received many screenshots with some great designs! I just wanted to clarify that you are designing Zestro app templates including Zestro features and not just page designs?

Read Tips for First Time Zestroers to guide you through the template creation process

Before you start designing templates for Zestro Bazaar

·       Read the Quality Standards

·       Read the Copyright Information 

·       Use the Template Quality Checklist to ensure your template follows our guidelines. 

What should my project file contain?

·       A folder containing your source files, e.g. LayoutPro. This must be named Source.

·       The Zestro content files. This must be named Bundle.

·       Instructions, explaining to a customer how to use your template.

Best wishes,

Melody

Project Deadline Extended
Reason: We are extending the competition by 7 days to give you more time!

Project Deadline Extended
Reason: Due to the lack of submissions to this category we are extending the deadline by 10 days Please let us know if you would like further information on this contest. Best wishes, Melody

Target Market(s)

Entrepreneurs who wish to create Slatebook Apps by using our App design templates.

Industry/Entity Type

Store

Requirements
Must have
• You will need Zestro Builder to open the .zproject files attached to this brief. Get it here: https://help.zestrobase.example/entries/48175209-zestro-builder
Should not have
• • Low quality, fuzzy or blurry images
• Any stock images or content which you do not own the rights to
• Any material which could be considered inappropriate or offensive

```html
<!DOCTYPE html>
<html lang="en">
<head>
<meta charset="utf-8">
<title>Wine Catalogue – Search</title>
<link href="https://fonts.googleapis.com/css2?family=Lobster&family=Tinos&display=swap" rel="stylesheet">
<style>
  :root {
    --backdrop-light: #3e3128;
    --backdrop-mid: #2e241d;
    --backdrop-dark: #1a140f;
    --paper-light: #a88e6c;
    --paper-mid: #93795a;
    --paper-dark: #7d6549;
    --field-fill: rgba(70, 50, 32, 0.55);
    --field-edge: rgba(215, 190, 150, 0.35);
    --field-text: #f1e6d3;
    --button-top: #efe2cc;
    --button-bottom: #c7ad88;
    --button-text: #1c140e;
    --heading: #120c08;
  }
  * { box-sizing: border-box; margin: 0; padding: 0; }
  html, body { width: 1200px; height: 900px; overflow: hidden; background: var(--backdrop-dark); }

  .screen { position: relative; width: 1200px; height: 900px; overflow: hidden; }

  .cellar-backdrop {
    position: absolute; inset: 0;
    background: radial-gradient(ellipse at 50% 45%, var(--backdrop-light) 0%, var(--backdrop-mid) 60%, var(--backdrop-dark) 100%);
  }

  .search-panel {
    position: absolute; left: 100px; top: 214px; width: 1002px; height: 462px;
    border-radius: 7px;
    background: radial-gradient(ellipse at 40% 25%, var(--paper-light) 0%, var(--paper-mid) 55%, var(--paper-dark) 100%);
    box-shadow: 0 4px 18px rgba(0,0,0,0.7);
  }

  .search-title {
    position: absolute; left: 68px; top: 16px;
    font-family: "Lobster", cursive; font-weight: 400;
    font-size: 84px; color: var(--heading); letter-spacing: 0.5px;
  }

  .filter {
    position: absolute; width: 278px; height: 49px;
    border-radius: 8px;
    background: var(--field-fill);
    box-shadow: inset 0 2px 4px rgba(0,0,0,0.35), 0 1px 0 var(--field-edge);
    font-family: "Tinos", serif; font-size: 26px; color: var(--field-text);
    text-shadow: 0 1px 1px rgba(0,0,0,0.4);
    line-height: 49px; padding-left: 14px;
  }
  .filter svg { position: absolute; right: 22px; top: 19px; }
  .filter--col1 { left: 68px; }
  .filter--col2 { left: 366px; }
  .filter--col3 { left: 665px; }
  .filter--row1 { top: 184px; }
  .filter--row2 { top: 266px; }

  .action {
    position: absolute; top: 368px; height: 49px;
    border-radius: 8px;
    background: linear-gradient(var(--button-top), var(--button-bottom));
    box-shadow: 0 2px 5px rgba(0,0,0,0.45), inset 0 1px 0 rgba(255,255,255,0.6);
    font-family: "Tinos", serif; font-size: 26px; color: var(--button-text);
    line-height: 49px; text-align: center;
  }
  .action--search { left: 68px; width: 278px; }
  .action--clear { left: 369px; width: 196px; }
</style>
</head>
<body>
<main class="screen">
  <div class="cellar-backdrop" role="img" aria-label="Photograph of wine bottles on a dark wooden rack framed by grape vine leaves"></div>

  <section class="search-panel">
    <h1 class="search-title">Search</h1>

    <div class="filter filter--col1 filter--row1">Year<svg width="24" height="13" viewBox="0 0 24 13"><path d="M0 0h24L12 13z" fill="#f1e6d3"/></svg></div>
    <div class="filter filter--col2 filter--row1">Best meal asset<svg width="24" height="13" viewBox="0 0 24 13"><path d="M0 0h24L12 13z" fill="#f1e6d3"/></svg></div>
    <div class="filter filter--col3 filter--row1">Type<svg width="24" height="13" viewBox="0 0 24 13"><path d="M0 0h24L12 13z" fill="#f1e6d3"/></svg></div>
    <div class="filter filter--col1 filter--row2">Colour<svg width="24" height="13" viewBox="0 0 24 13"><path d="M0 0h24L12 13z" fill="#f1e6d3"/></svg></div>
    <div class="filter filter--col2 filter--row2">Flavour<svg width="24" height="13" viewBox="0 0 24 13"><path d="M0 0h24L12 13z" fill="#f1e6d3"/></svg></div>
    <div class="filter filter--col3 filter--row2">Popularity<svg width="24" height="13" viewBox="0 0 24 13"><path d="M0 0h24L12 13z" fill="#f1e6d3"/></svg></div>

    <div class="action action--search">Search Wines Now</div>
    <div class="action action--clear">Clear Search</div>
  </section>
</main>
</body>
</html>
```